I Need a Banner for Web Advertising

impression banner for brivola AD
size 728x90, 320x50 , 160x600 , 300x600 , 100x50
Banner background bright blue
would like the AD to say -
We pay cash for houses in any condition
Probate,foreclosure, Pass due property taxes ect
470-555-0193
Updates
We would like to change the words to -
We pay cash for houses in any condition!
Probate, Foreclosure, Pass Due Property Taxes, and more!
470-555-0193
Target Market(s)
consumers that need to sale
Industry/Entity Type
Real Estate

```html
<!DOCTYPE html>
<html lang="en">
<head>
<meta charset="utf-8">
<title>Brivola Web Banner Set</title>
<link rel="stylesheet" href="https://fonts.googleapis.com/css2?family=Red+Hat+Display:wght@300;400;700;900&family=Gelasio:wght@400&display=swap">
<style>
  :root {
    --navy: #02036b;
    --blue: #0891cf;
    --orange: #f9a24b;
    --green: #9ccd3c;
    --yellow: #f7c600;
    --lime-text: #dcf23a;
    --pink: #f0145a;
    --ink: #111111;
    --white: #ffffff;
    --photo-warm-a: #b9ad96;
    --photo-warm-b: #8f8778;
    --photo-dusk-a: #9fb6d8;
    --photo-dusk-b: #4d5f80;
  }
  * { margin: 0; padding: 0; box-sizing: border-box; }
  html, body { width: 1200px; height: 1200px; overflow: hidden; background: var(--navy); }
  .canvas { position: relative; width: 1200px; height: 1200px; background: var(--navy); }
  .banner { position: absolute; display: block; overflow: hidden; }
  .banner--small-rect { left: 309px; top: 120px; width: 220px; height: 154px; }
  .banner--wide-rect { left: 583px; top: 120px; width: 308px; height: 154px; }
  .banner--leaderboard { left: 309px; top: 297px; width: 582px; height: 91px; }
  .banner--skyscraper { left: 309px; top: 408px; width: 179px; height: 671px; }
  .banner--half-page { left: 555px; top: 408px; width: 336px; height: 671px; }
  .fill-blue { fill: var(--blue); }
  .fill-orange { fill: var(--orange); }
  .fill-green { fill: var(--green); }
  .fill-pink { fill: var(--pink); }
  .brand-name { font-family: "Red Hat Display", sans-serif; font-weight: 900; fill: var(--ink); letter-spacing: 0.5px; }
  .head { font-family: "Red Hat Display", sans-serif; font-weight: 700; }
  .head-light { font-family: "Red Hat Display", sans-serif; font-weight: 400; fill: var(--white); }
  .head-white { fill: var(--white); }
  .head-yellow { fill: var(--yellow); }
  .head-ink { fill: var(--ink); }
  .phone { font-family: "Red Hat Display", sans-serif; font-weight: 700; }
  .serif-copy { font-family: "Gelasio", serif; font-weight: 400; }
  .cta-label { font-family: "Red Hat Display", sans-serif; font-weight: 700; fill: var(--white); }
</style>
</head>
<body>
<main class="canvas">

  <!-- Small rectangle -->
  <svg class="banner banner--small-rect" viewBox="0 0 220 154" aria-label="Brivola small rectangle banner">
    <defs>
      <linearGradient id="warm-house-a" x1="0" y1="0" x2="0" y2="1">
        <stop offset="0" stop-color="var(--photo-warm-a)"/>
        <stop offset="1" stop-color="var(--photo-warm-b)"/>
      </linearGradient>
    </defs>
    <rect class="fill-blue" width="220" height="154"/>
    <rect x="27" y="35" width="193" height="119" fill="url(#warm-house-a)" role="img" aria-label="Photo of a two-storey suburban house with a porch and garage"/>
    <polygon class="fill-orange" points="0,35 61,154 0,154"/>
    <text class="brand-name" x="110" y="32" font-size="22" text-anchor="middle">BRIVOLA</text>
    <rect class="fill-orange" x="88" y="62" width="8" height="51" rx="3"/>
    <rect class="fill-green" x="91" y="62" width="129" height="51" rx="3"/>
    <text class="head head-white" x="204" y="73" font-size="6.2" text-anchor="end">WE PAID COST FOR HOUSES</text>
    <text class="head" x="204" y="82" font-size="6.2" text-anchor="end"><tspan class="head-white">IN </tspan><tspan class="head-ink">ANY CONDITION</tspan></text>
    <text class="serif-copy" x="158" y="98" font-size="5.8" fill="var(--ink)" text-anchor="middle">Probate, Facing for Closure,</text>
    <text class="serif-copy" x="158" y="105" font-size="5.8" fill="var(--ink)" text-anchor="middle">Pass due property taxes etc.......</text>
    <rect class="fill-pink" x="163" y="131" width="43" height="14" rx="3"/>
    <text class="cta-label" x="184.5" y="140.5" font-size="5.6" text-anchor="middle">Read More</text>
    <text class="phone" x="12" y="140" font-size="6.4" fill="var(--ink)" transform="rotate(-90 12 140)">470-555-0193</text>
  </svg>

  <!-- Wide rectangle -->
  <svg class="banner banner--wide-rect" viewBox="0 0 308 154" aria-label="Brivola wide rectangle banner">
    <defs>
      <linearGradient id="dusk-house-a" x1="0" y1="0" x2="1" y2="0">
        <stop offset="0" stop-color="var(--blue)" stop-opacity="0"/>
        <stop offset="0.25" stop-color="var(--photo-dusk-a)"/>
        <stop offset="1" stop-color="var(--photo-dusk-b)"/>
      </linearGradient>
    </defs>
    <rect class="fill-blue" width="308" height="154"/>
    <rect x="131" y="0" width="177" height="154" fill="url(#dusk-house-a)" role="img" aria-label="Photo of a blue two-storey house at dusk with a lit porch"/>
    <polygon class="fill-orange" points="0,29 72,154 0,154"/>
    <text class="brand-name" x="22" y="34" font-size="24">BRIVOLA</text>
    <text class="head-light" x="45" y="61" font-size="8.5">WE PAID COST</text>
    <text class="head head-yellow" x="45" y="79" font-size="14">FOR HOUSES IN</text>
    <text class="head head-white" x="45" y="93" font-size="11.5">ANY CONDITION</text>
    <rect class="fill-green" x="0" y="122" width="308" height="18"/>
    <text class="serif-copy" x="16" y="135" font-size="10.5" fill="var(--ink)">Probate, Facing for Closure, Pass due property taxes etc.......</text>
  </svg>

  <!-- Leaderboard -->
  <svg class="banner banner--leaderboard" viewBox="0 0 582 91" aria-label="Brivola leaderboard banner">
    <defs>
      <linearGradient id="dusk-house-b" x1="0" y1="0" x2="1" y2="0">
        <stop offset="0" stop-color="var(--blue)" stop-opacity="0"/>
        <stop offset="0.3" stop-color="var(--photo-dusk-a)"/>
        <stop offset="1" stop-color="var(--photo-dusk-b)"/>
      </linearGradient>
    </defs>
    <rect class="fill-blue" width="582" height="91"/>
    <rect x="380" y="0" width="202" height="91" fill="url(#dusk-house-b)" role="img" aria-label="Photo of a blue two-storey house at dusk"/>
    <polygon class="fill-orange" points="0,0 19,0 96,91 0,91"/>
    <polygon class="fill-orange" points="486,0 582,0 582,41"/>
    <text class="head head-white" x="92" y="19" font-size="13">WE PAID COST FOR HOUSES IN ANY CONDITION</text>
    <text class="serif-copy" x="92" y="34" font-size="10" fill="var(--lime-text)">Probate, Facing for Closure, Pass due property taxes etc.......</text>
    <text class="brand-name" x="238" y="82" font-size="33" text-anchor="middle">BRIVOLA</text>
    <text class="phone" x="15" y="85" font-size="9" fill="var(--ink)">470-555-0193</text>
    <rect class="fill-pink" x="380" y="70" width="39" height="11" rx="2.5"/>
    <text class="cta-label" x="399.5" y="77.8" font-size="5.4" text-anchor="middle">Read More</text>
  </svg>

  <!-- Skyscraper -->
  <svg class="banner banner--skyscraper" viewBox="0 0 179 671" aria-label="Brivola skyscraper banner">
    <defs>
      <linearGradient id="dusk-house-c" x1="0" y1="0" x2="0" y2="1">
        <stop offset="0" stop-color="var(--photo-dusk-a)"/>
        <stop offset="1" stop-color="var(--photo-dusk-b)"/>
      </linearGradient>
    </defs>
    <rect class="fill-blue" width="179" height="671"/>
    <text class="brand-name" x="89.5" y="50" font-size="21" text-anchor="middle">BRIVOLA</text>
    <text class="head-light" x="89.5" y="115" font-size="13" text-anchor="middle">WE PAID COST</text>
    <text class="head head-yellow" x="89.5" y="137" font-size="22" text-anchor="middle">FOR HOUSES</text>
    <text class="head head-yellow" x="89.5" y="157" font-size="15" text-anchor="middle">IN</text>
    <text class="head head-white" x="89.5" y="181" font-size="17.5" text-anchor="middle">ANY CONDITION</text>
    <polygon class="fill-orange" points="179,216 179,245 40,245"/>
    <polygon points="0,258 179,238 179,423 0,440" fill="url(#dusk-house-c)" role="img" aria-label="Photo of a blue two-storey house with a lit garage at dusk"/>
    <polygon class="fill-orange" points="0,423 179,423 0,462"/>
    <polygon class="fill-green" points="0,471 179,471 179,605 0,585"/>
    <text class="serif-copy" x="89.5" y="517" font-size="15" fill="var(--white)" text-anchor="middle">Probate,</text>
    <text class="serif-copy" x="89.5" y="534" font-size="15" fill="var(--white)" text-anchor="middle">Facing for Closure,</text>
    <text class="serif-copy" x="89.5" y="551" font-size="15" fill="var(--white)" text-anchor="middle">Pass due</text>
    <text class="serif-copy" x="89.5" y="568" font-size="15" fill="var(--white)" text-anchor="middle">property taxes etc.......</text>
    <rect class="fill-orange" x="0" y="633" width="179" height="29"/>
    <text class="phone" x="89.5" y="654" font-size="18" fill="var(--ink)" text-anchor="middle">470-555-0193</text>
    <rect class="fill-pink" x="105" y="403" width="60" height="16" rx="4"/>
    <text class="cta-label" x="135" y="414.5" font-size="8.4" text-anchor="middle">Read More</text>
  </svg>

  <!-- Half page -->
  <svg class="banner banner--half-page" viewBox="0 0 336 671" aria-label="Brivola half page banner">
    <defs>
      <linearGradient id="warm-house-b" x1="0" y1="0" x2="0" y2="1">
        <stop offset="0" stop-color="var(--photo-warm-a)"/>
        <stop offset="1" stop-color="var(--photo-warm-b)"/>
      </linearGradient>
    </defs>
    <rect class="fill-blue" width="336" height="671"/>
    <polygon points="0,73 336,100 336,406 0,337" fill="url(#warm-house-b)" role="img" aria-label="Photo of a beige two-storey house with a front porch and garage"/>
    <polygon class="fill-orange" points="0,0 336,0 336,163 0,46"/>
    <polygon class="fill-blue" points="126,26 336,26 336,59 154,59"/>
    <text class="phone head-white" x="233" y="51" font-size="21" text-anchor="middle">470-555-0193</text>
    <polygon class="fill-green" points="0,337 336,406 336,446"/>
    <rect class="fill-pink" x="230" y="343" width="82" height="22" rx="5"/>
    <text class="cta-label" x="271" y="358.5" font-size="11.5" text-anchor="middle">Read More</text>
    <text class="brand-name" x="32" y="410" font-size="44" transform="rotate(17 32 410)">BRIVOLA</text>
    <text class="head-light" x="34" y="503" font-size="21">WE PAID COST</text>
    <text class="head head-yellow" x="33" y="537" font-size="36">FOR HOUSES IN</text>
    <text class="head head-white" x="34" y="568" font-size="28">ANY CONDITION</text>
    <rect class="fill-green" x="0" y="587" width="336" height="56"/>
    <text class="serif-copy" x="168" y="611" font-size="16" fill="var(--white)" text-anchor="middle">Probate, Facing for Closure,</text>
    <text class="serif-copy" x="168" y="628" font-size="16" fill="var(--white)" text-anchor="middle">Pass due property taxes etc.......</text>
  </svg>

</main>
</body>
</html>
```